PLIVET Buck Slip: Request for Donations to our Program's Development Fund

We would like to create an invitation card/double sided pamplet (about 4x9 inches) to place in orthopaedics clinics and hand/mail out to potential donors about our research program, Westmere Study Group for Joint & Muscle Health. We have attached a copy of a design we've been working with but are looking for more of a professional touch.

Target Market(s)

Patients, Donors

Industry/Entity Type

Medical And Science

Font styles to use
Other font styles liked:
• Gothan Bold, Gotham Book, Gothan, Georgia, Serif, Sans Serif

Colors
ec1f27
f78f20
ffffff
000000
333333
5c5c5c
fbed22
fbee3d
ffc214

Requirements
Must have
• Please use the visual identity standards for guidance to help with colour choice and font selection (https://www.norvalenu.example/brand/system/files/1.0-logo-visual-identity_april2017.pdf)

```html
<!DOCTYPE html>
<html lang="en">
<head>
<meta charset="utf-8">
<title>PLIVET Buck Slip</title>
<link href="https://fonts.googleapis.com/css2?family=Montserrat:wght@400;500;600;700&family=Roboto:wght@400;500&display=swap" rel="stylesheet">
<style>
  :root {
    --red: #c8202b;
    --brand-red: #ec1f27;
    --yellow: #fbed22;
    --ink: #000000;
    --text: #333333;
    --grey: #5c5c5c;
    --band: #7b7e74;
    --panel: #f4f4f4;
    --rule: #c9c9c9;
    --stamp: #dcdcdc;
    --stage: #b9b9b9;
    --white: #ffffff;
  }
  * { margin: 0; padding: 0; box-sizing: border-box; }
  html, body { width: 1200px; height: 903px; overflow: hidden; }
  body { background: var(--stage); font-family: "Montserrat", sans-serif; color: var(--ink); position: relative; }

  .card { position: absolute; left: 190px; width: 820px; height: 365px; background: var(--white); overflow: hidden; }
  .card--front { top: 63px; }
  .card--back { top: 477px; }

  .hero-photo {
    position: absolute; inset: 0;
    background:
      radial-gradient(ellipse 150px 110px at 250px 220px, #5a3a2b 0%, #8a5e48 45%, rgba(180,150,135,0) 100%),
      radial-gradient(ellipse 220px 260px at 270px 150px, #9aa3b0 0%, rgba(200,210,220,0) 100%),
      linear-gradient(100deg, #7b8392 0%, #c8cfd8 45%, #eef1f4 70%, #dde6ec 100%);
  }

  .quote-box {
    position: absolute; left: 458px; top: 91px; width: 323px; height: 148px;
    background: var(--red); border-radius: 9px; color: var(--white);
    font-family: "Roboto", sans-serif;
  }
  .quote-box .mark { position: absolute; font-size: 20px; font-weight: 500; line-height: 1; }
  .quote-box .mark--open { left: 10px; top: 14px; }
  .quote-box .mark--close { left: 110px; top: 111px; }
  .quote-text { position: absolute; left: 26px; top: 22px; width: 283px; font-size: 15.2px; line-height: 18.4px; text-align: justify; }
  .quote-author { position: absolute; left: 154px; top: 111px; font-size: 15px; font-weight: 500; }

  .brand { position: absolute; display: flex; align-items: center; }
  .brand-name { font-weight: 700; color: var(--brand-red); letter-spacing: 1px; line-height: 1; }
  .brand-divider { width: 1px; background: #9a9a9a; opacity: .6; }
  .brand-unit { color: var(--ink); font-weight: 600; line-height: 1.05; }
  .brand-unit span { display: block; }
  .brand-unit span + span { font-weight: 500; letter-spacing: 0.6px; }

  .brand--front { left: 414px; top: 285px; }
  .brand--front .brand-name { font-size: 36px; }
  .brand--front .brand-divider { height: 46px; margin: 0 11px; }
  .brand--front .brand-unit { font-size: 12px; }

  .brand--back { left: 416px; top: 46px; }
  .brand--back .brand-name { font-size: 26px; }
  .brand--back .brand-divider { height: 30px; margin: 0 7px; }
  .brand--back .brand-unit { font-size: 8.4px; }

  .mission { position: absolute; left: 28px; top: 26px; }
  .mission h2 { font-size: 11.6px; font-weight: 500; }
  .mission ul { list-style: none; margin-top: 8px; }
  .mission li { font-size: 9.6px; color: var(--text); line-height: 17.6px; padding-left: 13px; position: relative; letter-spacing: .2px; }
  .mission li::before { content: ""; position: absolute; left: 1px; top: 7px; width: 4px; height: 4px; border-radius: 50%; background: var(--brand-red); }

  .appeal { position: absolute; left: 28px; top: 121px; width: 320px; font-size: 11.2px; line-height: 13.8px; color: var(--text); }
  .accent { color: var(--brand-red); font-weight: 500; }
  .contact { position: absolute; left: 28px; top: 187px; font-size: 11.2px; line-height: 15.4px; color: var(--text); }
  .contact strong { color: var(--ink); font-weight: 600; }

  .donate-band { position: absolute; left: 22px; top: 257px; width: 332px; height: 84px; background: var(--band); font-family: "Roboto", sans-serif; color: var(--white); padding: 22px 0 0 24px; font-size: 11.6px; line-height: 18px; }
  .donate-band .yes { color: #f7d842; }
  .donate-band .url { font-weight: 500; }

  .stamp-box { position: absolute; left: 709px; top: 23px; width: 67px; height: 77px; background: var(--stamp); }
  .address-line { position: absolute; left: 420px; width: 358px; height: 1.5px; background: var(--rule); }

  .partner-panel { position: absolute; left: 420px; top: 257px; width: 378px; height: 84px; background: var(--panel); font-family: "Roboto", sans-serif; }
  .qr-slot { position: absolute; left: 38px; top: 13px; width: 89px; height: 52px; border: 2px solid var(--grey); display: flex; align-items: center; justify-content: center; font-size: 9.8px; color: var(--ink); }
  .partner-label { position: absolute; left: 208px; top: 12px; font-size: 11.4px; color: var(--ink); }
  .partner-badge { position: absolute; }
  .partner-badge--uni { left: 200px; top: 34px; width: 24px; height: 28px; border-radius: 3px 3px 12px 12px; background: #c8a21a; }
  .partner-badge--health { left: 290px; top: 36px; width: 22px; height: 22px; background: #2a7fc1; }
</style>
</head>
<body>

  <section class="card card--front">
    <div class="hero-photo" role="img" aria-label="Photo of cupped hands holding soil with a small green seedling, soft pale background"></div>

    <blockquote class="quote-box">
      <span class="mark mark--open">&ldquo;</span>
      <p class="quote-text">Modern medical advances have helped millions of people live longer, healthier lives. We owe these improvements to decades of investment in medical research</p>
      <span class="mark mark--close">&rdquo;</span>
      <cite class="quote-author">-Dale Harwick</cite>
    </blockquote>

    <div class="brand brand--front">
      <span class="brand-name">PLIVET</span>
      <span class="brand-divider"></span>
      <p class="brand-unit"><span>Westmere Study Group</span><span>for Joint &amp; Muscle Health</span></p>
    </div>
  </section>

  <section class="card card--back">
    <div class="mission">
      <h2>We are passionate clinicians and educators focused on</h2>
      <ul>
        <li>Empowering patients</li>
        <li>Advancing research</li>
        <li>Improving clinical care</li>
      </ul>
    </div>

    <p class="appeal"><span class="accent">We need your help!</span> Donations help run the PLIVET research program and without your support, it simply wouldn&rsquo;t be possible.</p>

    <div class="contact">
      <p class="accent">To learn more, talk to your surgeon or contact us:</p>
      <p><strong>Phone:</strong> 555-014-2290</p>
      <p><strong>Email:</strong> plivetresearch@norvalenu.example</p>
    </div>

    <div class="donate-band">
      <p><span class="yes">YES, I would like to help!</span> Visit the following link:</p>
      <p class="url">https://give.norvalenu.example/medicine/PLIVET</p>
    </div>

    <div class="brand brand--back">
      <span class="brand-name">PLIVET</span>
      <span class="brand-divider"></span>
      <p class="brand-unit"><span>Westmere Study Group</span><span>for Joint &amp; Muscle Health</span></p>
    </div>

    <div class="stamp-box"></div>
    <div class="address-line" style="top:143px"></div>
    <div class="address-line" style="top:182px"></div>
    <div class="address-line" style="top:221px"></div>

    <div class="partner-panel">
      <div class="qr-slot">QR CODE HERE</div>
      <p class="partner-label">In partnership with:</p>
      <div class="partner-badge partner-badge--uni"></div>
      <div class="partner-badge partner-badge--health"></div>
    </div>
  </section>

</body>
</html>
```